" Montamos roteiros turisticos especializados em experiência. Inicialmente a empresa ofertará roteiros especializados para fotografia, porém no futuro poderá conter roteiros para vinhos, culinária, esportes, etc. "

```html
<!DOCTYPE html>
<html lang="pt-BR">
<head>
<meta charset="UTF-8">
<title>Trilhar Expedições — Bali | Templos e Paisagens</title>
<link href="https://fonts.googleapis.com/css2?family=Montserrat:wght@400;600;700;800&display=swap" rel="stylesheet">
<style>
  :root {
    --stage: #e9ebec;
    --white: #ffffff;
    --ink: #3a4650;
    --muted: #8a96a0;
    --brand: #1f6fa8;
    --accent: #f6a623;
    --accent-dark: #e8901a;
    --badge: rgba(30, 136, 201, 0.88);
    --sky-top: #5f9fce;
    --sky-mid: #a9c9dc;
    --hills: #4f7d4c;
    --water: #3f6f63;
  }
  * { margin: 0; padding: 0; box-sizing: border-box; }
  html, body { width: 1200px; height: 1200px; overflow: hidden; }
  body {
    background: var(--stage);
    font-family: "Montserrat", sans-serif;
    position: relative;
  }
  .page {
    position: absolute;
    left: 0; top: 237px;
    width: 1200px; height: 725px;
    background: var(--white);
    overflow: hidden;
  }
  .site-header {
    height: 121px;
    display: flex;
    align-items: center;
    justify-content: space-between;
    padding: 0 48px;
    background: var(--white);
  }
  .brand { display: flex; align-items: center; gap: 14px; }
  .brand-dot { width: 38px; height: 38px; border-radius: 50%; background: var(--accent); }
  .brand-name { font-size: 30px; font-weight: 600; color: var(--brand); letter-spacing: -0.5px; }
  .main-nav { display: flex; align-items: center; gap: 34px; }
  .main-nav a {
    font-size: 13px; font-weight: 700; color: var(--ink);
    text-decoration: none; text-transform: uppercase; letter-spacing: 0.4px;
  }
  .nav-icon { width: 20px; height: 20px; }
  .hero {
    position: relative;
    height: 604px;
    text-align: center;
    color: var(--white);
  }
  .hero-photo {
    position: absolute; inset: 0;
    background:
      linear-gradient(180deg, rgba(0,0,0,0) 55%, rgba(0,0,0,0.25) 100%),
      linear-gradient(180deg, var(--sky-top) 0%, var(--sky-mid) 38%, var(--hills) 58%, var(--water) 80%, #2f5a4b 100%);
  }
  .hero-content { position: relative; padding-top: 48px; }
  .hero-title {
    font-size: 44px; font-weight: 800; color: var(--accent);
    letter-spacing: 0.5px; text-transform: uppercase;
    text-shadow: 0 2px 6px rgba(0,0,0,0.25);
  }
  .breadcrumb { margin-top: 8px; font-size: 13px; color: var(--white); opacity: 0.9; }
  .hero-lead {
    margin: 26px auto 0; width: 560px;
    font-size: 22px; line-height: 1.4; font-weight: 400;
    text-shadow: 0 1px 4px rgba(0,0,0,0.35);
  }
  .cta {
    display: inline-flex; align-items: center; gap: 10px;
    margin-top: 40px; padding: 13px 40px;
    background: var(--accent); border-radius: 4px;
    font-size: 14px; font-weight: 700; letter-spacing: 0.6px;
    color: var(--white); text-transform: uppercase;
    box-shadow: 0 3px 0 var(--accent-dark);
  }
  .trip-facts {
    display: flex; justify-content: center; gap: 66px;
    margin-top: 62px;
  }
  .fact { width: 140px; display: flex; flex-direction: column; align-items: center; }
  .fact-badge {
    width: 140px; height: 140px; border-radius: 50%;
    background: var(--badge);
    border: 3px solid rgba(255,255,255,0.55);
    display: flex; flex-direction: column; align-items: center; justify-content: center;
    line-height: 1;
  }
  .fact-value { font-size: 46px; font-weight: 700; }
  .fact-unit { font-size: 20px; font-weight: 600; margin-top: 6px; text-transform: uppercase; }
  .fact-value.is-word { font-size: 30px; text-transform: uppercase; }
  .fact-photo {
    background: radial-gradient(circle at 50% 40%, #9fc4e0 0%, #5a89b4 60%, #3b6790 100%);
  }
  .fact-label {
    margin-top: 16px; font-size: 13px; font-weight: 700;
    text-transform: uppercase; letter-spacing: 0.5px;
  }
</style>
</head>
<body>
  <main class="page">
    <header class="site-header">
      <div class="brand">
        <span class="brand-dot"></span>
        <span class="brand-name">Trilhar Expedições</span>
      </div>
      <nav class="main-nav">
        <svg class="nav-icon" viewBox="0 0 20 20" aria-label="Início"><path d="M3 10 L10 3 L17 10 M5 9 V17 H15 V9" fill="none" stroke="#8a96a0" stroke-width="2"/></svg>
        <a href="#">Sobre nós</a>
        <a href="#">Próximas expedições</a>
        <a href="#">Últimas viagens</a>
        <a href="#">FAQ</a>
        <a href="#">Contato</a>
        <svg class="nav-icon" viewBox="0 0 20 20" aria-label="Buscar"><circle cx="8" cy="8" r="5.5" fill="none" stroke="#1e88c9" stroke-width="2"/><path d="M12 12 L17 17" stroke="#1e88c9" stroke-width="2.2" stroke-linecap="round"/></svg>
      </nav>
    </header>

    <section class="hero">
      <div class="hero-photo" role="img" aria-label="Fotografia de templo balinês à beira de um lago com montanhas e céu azul"></div>
      <div class="hero-content">
        <h1 class="hero-title">Bali | Templos e Paisagens</h1>
        <p class="breadcrumb">Home / Próximas Expedições / Bali</p>
        <p class="hero-lead">Um dos roteiros mais cobiçados por viajantes e fotógrafos de todo o mundo</p>
        <span class="cta">Garanta sua vaga
          <svg width="14" height="14" viewBox="0 0 14 14"><path d="M2 7 H11 M7 3 L11 7 L7 11" fill="none" stroke="#fff" stroke-width="2"/></svg>
        </span>

        <div class="trip-facts">
          <div class="fact">
            <div class="fact-badge"><span class="fact-value">09</span><span class="fact-unit">Dias</span></div>
            <span class="fact-label">Duração</span>
          </div>
          <div class="fact">
            <div class="fact-badge"><span class="fact-value">02</span><span class="fact-unit">Vagas</span></div>
            <span class="fact-label">Disponibilidade</span>
          </div>
          <div class="fact">
            <div class="fact-badge"><span class="fact-value is-word">Fev</span><span class="fact-unit">2018</span></div>
            <span class="fact-label">Quando</span>
          </div>
          <div class="fact">
            <div class="fact-badge"><span class="fact-value is-word">Expert</span></div>
            <span class="fact-label">Nível</span>
          </div>
          <div class="fact">
            <div class="fact-badge fact-photo" role="img" aria-label="Retrato do fotógrafo guia da expedição"></div>
            <span class="fact-label">Fotógrafo</span>
          </div>
        </div>
      </div>
    </section>
  </main>
</body>
</html>
```